Business Card Design Project

I need a new business card design for my building/development company: Ridgewell Constructions.

We specialise in small sub-divisions, multi-story developments and new house builds.
We handle the whole process from concept stage right throught to a fully developed property.
Updates

Project Deadline Extended
Reason: Need a couple of extra days to decide as there are so many amazing designs

Target Market(s)

people looking to develop their property and need help. New property buyers

Industry/Entity Type

House

Requirements
Must have
• My logo on both sides:
Side 1: Logo taking up whole side as per old card but with a color/style change.

Side 2: Contact page: include logo but the rest just surprise me!

All contact details will be: (and need to be changable for each employee) I'll inform you of specifics before printing.

Name Surname
Position ie. Managing director
M: insert mobile
E: insert email
P.O. Box 518, Elmhurst, Vic, 3145
www.ridgewellconstructions.com.au

Nice to have
• Colors i'd like: (not necessarily all but this is the basic idea)

Black, blue, grey, silver, white

```html
<!DOCTYPE html>
<html lang="en">
<head>
<meta charset="utf-8">
<title>Ridgewell Constructions – Business Card</title>
<link href="https://fonts.googleapis.com/css2?family=Arimo:wght@400;700&display=swap" rel="stylesheet">
<style>
  :root {
    --blue: #1d93d8;
    --blue-light: #5ab4e8;
    --ink: #1a1a1a;
    --white: #ffffff;
    --tint: #f3f4f5;
    --stage: #e6e8ea;
    --rule: rgba(255,255,255,0.55);
  }
  * { box-sizing: border-box; margin: 0; padding: 0; }
  html, body { width: 1200px; height: 900px; overflow: hidden; }
  body {
    background: var(--stage);
    font-family: "Arimo", Arial, sans-serif;
    position: relative;
  }
  .card {
    position: absolute;
    left: 250px;
    width: 700px;
    height: 400px;
    background: var(--white);
    overflow: hidden;
    box-shadow: 0 6px 20px rgba(0,0,0,0.12);
  }
  .card--front { top: 40px; }
  .card--back { top: 460px; }
  .card__texture { position: absolute; inset: 0; background: var(--tint); }
  .card__shapes { position: absolute; inset: 0; }

  .brand { position: absolute; color: var(--blue); font-weight: 700; line-height: 1; }
  .brand__mark { display: inline-block; background: var(--blue); vertical-align: middle; }
  .brand__tagline { display: block; color: var(--ink); font-weight: 400; }

  .card--front .brand { right: 48px; top: 150px; font-size: 44px; text-align: right; }
  .card--front .brand__mark { width: 34px; height: 34px; margin-right: 14px; }
  .card--front .brand__tagline { font-size: 15px; margin-top: 10px; letter-spacing: 0.3px; }

  .card--back .brand { left: 44px; top: 64px; font-size: 32px; }
  .card--back .brand__mark { width: 26px; height: 26px; margin-right: 12px; }
  .card--back .brand__tagline { font-size: 12px; margin: 6px 0 0 38px; }

  .person { position: absolute; left: 44px; bottom: 38px; color: var(--white); }
  .person__name { font-size: 20px; font-weight: 700; }
  .person__role { font-size: 14px; margin-top: 4px; }
  .person__address { font-size: 14px; margin-top: 22px; }

  .contact {
    position: absolute; right: 36px; bottom: 38px;
    color: var(--white); font-size: 14px;
    list-style: none;
    border-left: 1px solid var(--rule);
    padding-left: 16px;
  }
  .contact li { margin-top: 10px; }
  .contact li:first-child { margin-top: 0; }
  .contact__label { display: inline-block; width: 22px; font-weight: 700; }
</style>
</head>
<body>

<section class="card card--front" aria-label="Card front">
  <div class="card__texture" role="img" aria-label="Faint repeating brand-mark background pattern"></div>
  <svg class="card__shapes" viewBox="0 0 700 400" aria-hidden="true">
    <defs>
      <linearGradient id="frontBand" x1="0" y1="0" x2="1" y2="1">
        <stop offset="0" stop-color="#1d93d8"/>
        <stop offset="1" stop-color="#5ab4e8"/>
      </linearGradient>
    </defs>
    <polygon points="0,0 230,0 0,120" fill="url(#frontBand)"/>
  </svg>
  <div class="brand">
    <span class="brand__mark"></span>Ridgewell Constructions
    <span class="brand__tagline">renovation-construction-development</span>
  </div>
</section>

<section class="card card--back" aria-label="Card back">
  <div class="card__texture" role="img" aria-label="Faint repeating brand-mark background pattern"></div>
  <svg class="card__shapes" viewBox="0 0 700 400" aria-hidden="true">
    <defs>
      <linearGradient id="backBand" x1="0" y1="0" x2="1" y2="0">
        <stop offset="0" stop-color="#1d93d8"/>
        <stop offset="1" stop-color="#5ab4e8"/>
      </linearGradient>
    </defs>
    <polygon points="0,220 190,220 205,205 220,220 700,160 700,400 0,400" fill="url(#backBand)"/>
  </svg>
  <div class="brand">
    <span class="brand__mark"></span>Ridgewell Constructions
    <span class="brand__tagline">renovation-construction-development</span>
  </div>
  <div class="person">
    <p class="person__name">Megan Carlisle</p>
    <p class="person__role">Managing director</p>
    <p class="person__address">P.O. Box 518, Elmhurst, Vic, 3145</p>
  </div>
  <ul class="contact">
    <li><span class="contact__label">M:</span>0000 000 000</li>
    <li><span class="contact__label">E:</span>info@ridgewellconstructions.com.au</li>
    <li><span class="contact__label">W:</span>www.ridgewellconstructions.com.au</li>
  </ul>
</section>

</body>
</html>
```